Blue Finch Journeys

We are a predominantly online travel agency with high-end (first/business class) clients. I'm looking to either have our existing logo revamped or a new logo created with business card layout. I prefer to work with existing logo if possible so it remains familiar with existing clientele. I have uploaded a yellow business card layout showing icons on one side of the card. I would like to keep my existing colours, not yellow. could the company name/tag line go over the icons?
Business
Colette Draybin
Director
(I.A.T.A. 07815536)
(Vonsarel Pty. Ltd) ABN 61 574 203 819
412/58 Calderwood Street
Larkfield Bay | NSW 2584 | Australia
www.bluefinchjourneys.com.au
m: + 61 (0) 455 318 906
t: + 61 (0) 2 8471 2063
e: colette@bluefinchjourneys.com.au

```html
<!DOCTYPE html>
<html lang="en">
<head>
<meta charset="utf-8">
<title>Blue Finch Journeys — Business Card</title>
<link href="https://fonts.googleapis.com/css2?family=Cormorant+Garamond:wght@500&family=Work+Sans:wght@400;500&display=swap" rel="stylesheet">
<style>
  :root {
    --backdrop: #0f0f0f;
    --card: #1e1e1e;
    --card-edge: #262626;
    --gold: #ecbd8c;
    --silver: #cfcfcf;
    --emboss: #343434;
    --text-light: #f1f1f1;
    --rule-dim: #4a4a4a;
  }
  * { margin: 0; padding: 0; box-sizing: border-box; }
  html, body {
    width: 1200px; height: 900px; overflow: hidden;
    background: var(--backdrop);
  }
  .canvas {
    width: 1200px; height: 900px;
    display: flex; flex-direction: column; align-items: center; justify-content: center;
    gap: 40px;
  }
  .card {
    width: 700px; height: 380px;
    background: linear-gradient(160deg, var(--card-edge), var(--card) 60%);
    border-bottom: 4px solid var(--gold);
    position: relative;
    font-family: "Work Sans", sans-serif;
    color: var(--text-light);
  }
  /* front */
  .card-front { display: flex; flex-direction: column; align-items: center; }
  .brand {
    margin-top: 110px;
    display: flex; flex-direction: column; align-items: center;
  }
  .brand-name {
    font-family: "Cormorant Garamond", serif;
    font-weight: 500;
    font-size: 58px;
    line-height: 1;
    color: var(--silver);
    white-space: nowrap;
  }
  .brand-rule {
    width: 460px; height: 1px; background: var(--rule-dim);
    margin: 14px 0 10px;
  }
  .brand-tagline {
    font-size: 24px; letter-spacing: 6px; color: var(--emboss);
    text-shadow: 0 1px 0 #3a3a3a, 0 -1px 0 #111;
    white-space: nowrap;
  }
  .front-web {
    position: absolute; bottom: 40px; left: 0; right: 0; text-align: center;
    font-size: 15px; letter-spacing: 4px;
  }
  /* back */
  .card-back { display: flex; align-items: center; }
  .back-brand {
    width: 340px; display: flex; flex-direction: column; align-items: center;
  }
  .back-brand .brand-name { font-size: 36px; color: var(--gold); }
  .back-brand .brand-rule { width: 270px; background: var(--gold); opacity: .6; margin: 10px 0 8px; }
  .back-brand .brand-tagline { font-size: 15px; letter-spacing: 3px; color: var(--gold); text-shadow: none; }
  .divider { width: 2px; height: 260px; background: var(--gold); }
  .details { padding-left: 30px; font-size: 15px; line-height: 1.3; }
  .person-name {
    font-family: "Cormorant Garamond", serif; font-weight: 500;
    font-size: 26px; color: var(--gold); margin-bottom: 4px;
  }
  .block { margin-bottom: 12px; }
  .contact-list { list-style: none; }
  .contact-list li { display: flex; align-items: center; gap: 12px; white-space: nowrap; }
  .contact-list svg { width: 14px; height: 14px; fill: var(--gold); flex: none; }
</style>
</head>
<body>
<main class="canvas">
  <section class="card card-front">
    <div class="brand">
      <span class="brand-name">Blue Finch Journeys</span>
      <span class="brand-rule"></span>
      <span class="brand-tagline">travel at your pace</span>
    </div>
    <p class="front-web">www.bluefinchjourneys.com.au</p>
  </section>

  <section class="card card-back">
    <div class="back-brand">
      <span class="brand-name">Blue Finch Journeys</span>
      <span class="brand-rule"></span>
      <span class="brand-tagline">travel at your pace</span>
    </div>
    <div class="divider"></div>
    <div class="details">
      <p class="person-name">Colette Draybin</p>
      <div class="block">
        <p>Director (I.A.T.A. 07815536)</p>
        <p>ABN 61 574 203 819</p>
      </div>
      <div class="block">
        <p>412/58 Calderwood Street</p>
        <p>Larkfield Bay | NSW 2584</p>
        <p>Australia</p>
      </div>
      <ul class="contact-list">
        <li><svg viewBox="0 0 16 16"><path d="M4 0h8a1 1 0 0 1 1 1v14a1 1 0 0 1-1 1H4a1 1 0 0 1-1-1V1a1 1 0 0 1 1-1zm1 2v10h6V2zm3 11a1 1 0 1 0 0 2 1 1 0 0 0 0-2z"/></svg>+ 61 (0) 455 318 906</li>
        <li><svg viewBox="0 0 16 16"><path d="M3 1l3 3-2 2c1 2 4 5 6 6l2-2 3 3-2 2C7 15 1 9 1 3z"/></svg>+ 61 (0) 2 8471 2063</li>
        <li><svg viewBox="0 0 16 16"><path d="M1 3h14v1L8 9 1 4zm0 3l7 5 7-5v7H1z"/></svg>colette@bluefinchjourneys.com.au</li>
        <li><svg viewBox="0 0 16 16"><path d="M8 1a7 7 0 1 0 0 14A7 7 0 0 0 8 1zm-1 1.2V5H4.3A6 6 0 0 1 7 2.2zm2 0A6 6 0 0 1 11.7 5H9zM3.7 6H7v1.5H3.1a6 6 0 0 1 .6-1.5zM9 6h3.3a6 6 0 0 1 .6 1.5H9zM3.1 8.5H7V10H3.7a6 6 0 0 1-.6-1.5zm5.9 0h3.9a6 6 0 0 1-.6 1.5H9zM4.3 11H7v2.8A6 6 0 0 1 4.3 11zM9 11h2.7A6 6 0 0 1 9 13.8z"/></svg>www.bluefinchjourneys.com.au</li>
      </ul>
    </div>
  </section>
</main>
</body>
</html>
```